B2B EDM Banner Design- Specialist Tech Company

We need a new top-of-email banner for our EDM campaigns for Varnel Brix (www.varnelbrix-example.com
). This banner will sit at the top of every email and must immediately signal the brand, look modern and professional, and be visually aligned with the tech/IT audience.
Size of the banner: Around 728x90 - it must fit at the top of an email blast.
Purpose of the Banner
Establish a strong, recognizable brand identity across all Varnel Brix EDMs
visually consistent with existing banners created for other brands (see reference examples provided)
Communicate Varnel Brix’s value proposition at a glance
Brand Name
Varnel Brix
Tagline (must appear in the banner)
“11,322 whitepapers from 726 companies”
Design Requirements
Style & Tone
Modern, clean, and professional
Tech-centric look and feel
High-quality, sleek, and corporate
Eye-catching but not cluttered
Should feel premium and authoritative
Layout & Composition
Full-width banner for email header
Horizontal orientation similar to the Plomtar and Quindle Staff Archive examples
Include space for the brand name/logo prominently on the left or centered
Integrate the tagline in a readable, secondary position
Optional: a subtle background texture or tech-related abstract pattern (circuitry, network nodes, gradient, etc.)
No busy imagery—should feel clean and trustworthy
Color Palette
Use colors consistent with Varnel Brix branding from www.varnelbrix-example.com
Blues, greys, blacks, and tech-style gradients preferred
Should feel consistent with a B2B IT audience
Typography
Clean, sans-serif fonts (professional/tech-aligned)
Brand name should be bold and prominent
Tagline should be smaller, but still readable on desktop and mobile
Imagery (if used)
Abstract tech shapes, network visuals, geometric patterns, or gradient overlays
Avoid photography of people
Keep imagery subtle so text remains legible
Call-to-Action Button (optional)
None required in this banner (unlike the HR examples)
Banner should remain a pure brand header
Deliverables
Final banner in PNG and JPG formats
2–3 design variations (if possible) for A/B testing
Dimensions optimized for EDM: ~600–700px wide (standard email width), proportionate height

```html
<!DOCTYPE html>
<html lang="en">
<head>
<meta charset="utf-8">
<title>Varnel Brix – EDM Header Banner</title>
<link rel="stylesheet" href="https://fonts.googleapis.com/css2?family=Roboto:wght@400;700;900&display=swap">
<style>
  :root {
    --page-bg: #e6e6e6;
    --banner-bg: #0d1120;
    --brand-blue: #139fd9;
    --network-deep: #06102e;
    --network-mid: #0b2a6e;
    --network-glow: #1a4fb0;
    --text-light: #ffffff;
    --text-muted: #c9d6ea;
  }
  * { margin: 0; padding: 0; box-sizing: border-box; }
  html, body {
    width: 1200px;
    height: 322px;
    overflow: hidden;
    background: var(--page-bg);
    font-family: "Roboto", Arial, sans-serif;
  }
  .edm-banner {
    position: absolute;
    left: 83px;
    top: 97px;
    width: 1034px;
    height: 128px;
    background: var(--banner-bg);
    overflow: hidden;
  }
  .banner-art {
    position: absolute;
    inset: 0;
    width: 100%;
    height: 100%;
  }
  .brand-lockup {
    position: absolute;
    left: 26px;
    top: 40px;
    display: flex;
    align-items: center;
    gap: 12px;
  }
  .brand-dot {
    width: 48px;
    height: 48px;
    border-radius: 50%;
    background: var(--brand-blue);
    flex: none;
  }
  .brand-text { display: flex; flex-direction: column; }
  .brand-name {
    font-weight: 700;
    font-size: 25px;
    line-height: 1;
    color: var(--text-light);
    text-transform: uppercase;
    letter-spacing: 0.2px;
  }
  .brand-tagline {
    margin-top: 6px;
    padding-top: 3px;
    border-top: 1px solid var(--brand-blue);
    font-size: 7.5px;
    font-weight: 700;
    letter-spacing: 3.1px;
    color: var(--text-muted);
    text-transform: uppercase;
  }
  .value-prop {
    position: absolute;
    left: 385px;
    top: 25px;
    text-transform: uppercase;
  }
  .value-prop-line1 {
    display: block;
    font-weight: 400;
    font-size: 29px;
    line-height: 1;
    color: var(--text-light);
    letter-spacing: 0.2px;
  }
  .value-prop-line2 {
    display: block;
    margin-top: 2px;
    font-weight: 900;
    font-size: 47px;
    line-height: 1;
    color: var(--brand-blue);
  }
  .site-link {
    position: absolute;
    left: 771px;
    top: 45px;
    width: 242px;
    height: 38px;
    border-radius: 19px;
    background: var(--brand-blue);
    color: var(--text-light);
    font-weight: 700;
    font-size: 15px;
    display: flex;
    align-items: center;
    justify-content: center;
    text-decoration: none;
  }
</style>
</head>
<body>
  <header class="edm-banner">
    <svg class="banner-art" viewBox="0 0 1034 128" preserveAspectRatio="none" aria-hidden="false">
      <defs>
        <radialGradient id="network-tone" cx="0.45" cy="0.45" r="0.7">
          <stop offset="0" stop-color="var(--network-glow)"/>
          <stop offset="0.5" stop-color="var(--network-mid)"/>
          <stop offset="1" stop-color="var(--network-deep)"/>
        </radialGradient>
      </defs>
      <path class="network-backdrop" role="img" aria-label="Abstract blue network of connected nodes"
            d="M0,0 L313,0 C345,40 335,100 238,128 L0,128 Z" fill="url(#network-tone)"/>
      <path class="swoosh-inner" d="M313,0 L329,0 C352,40 345,98 295,128 L238,128 C335,100 345,40 313,0 Z" fill="var(--brand-blue)"/>
      <path class="swoosh-outer" d="M340,0 L356,0 C388,40 384,96 330,128 L307,128 C368,98 372,40 340,0 Z" fill="var(--brand-blue)"/>
    </svg>

    <div class="brand-lockup">
      <span class="brand-dot"></span>
      <div class="brand-text">
        <span class="brand-name">Varnel Brix</span>
        <span class="brand-tagline">For IT Professionals</span>
      </div>
    </div>

    <h1 class="value-prop">
      <span class="value-prop-line1">11,322 Whitepapers from</span>
      <span class="value-prop-line2">726 Companies</span>
    </h1>

    <a class="site-link" href="#">www.varnelbrix-example.com</a>
  </header>
</body>
</html>
```